Webdesign für Holding-Firma
Zielgruppe
Die velunto Holding ist eine Holding-Firma mit drei Tochtergesellschaften: velunto trusted advisors, velutno Real estate und Velunto GmbH. Wir haben Beteiligungen in IT-Unternehmen, Real Estate sowie kleine und mittlere Startups.
Aufgabenstellung
Das Design sollte nicht zu bunt sein und eher schlicht und futuristisch gestaltet sein. Gerne können die Farben aus den verschiedenen Logos verarbeitet werden.

```html
<!DOCTYPE html>
<html lang="de">
<head>
<meta charset="utf-8">
<title>Velunto Trusted Advisors</title>
<link rel="stylesheet" href="https://fonts.googleapis.com/css2?family=Roboto:wght@300;400;500;700&family=Roboto+Condensed:wght@700&family=Open+Sans:wght@300;700&display=swap">
<style>
  :root {
    --gold: #e0a33a;
    --gold-dark: #d8951f;
    --yellow: #f6d21a;
    --ink: #222;
    --muted: #555;
    --topbar: #f3f3f3;
    --cream: #faeedb;
    --footer: #fcd896;
    --line: #e6e6e6;
  }
  * { box-sizing: border-box; margin: 0; padding: 0; }
  html, body { width: 873px; height: 1200px; overflow: hidden; background: #fff; }
  body { font-family: "Roboto", sans-serif; color: var(--ink); position: relative; }

  .topbar { height: 26px; background: var(--topbar); border-bottom: 1px solid var(--line);
    display: flex; justify-content: space-between; align-items: center; padding: 0 117px; font-size: 9px; color: var(--muted); }
  .topbar .item { display: flex; align-items: center; gap: 6px; }
  .topbar svg { width: 11px; height: 11px; }

  .header { height: 61px; display: flex; align-items: center; padding: 0 117px; position: relative; }
  .brand { display: flex; align-items: center; gap: 10px; }
  .brand-mark { width: 14px; height: 14px; background: var(--gold); }
  .brand-name { font-size: 21px; font-weight: 700; letter-spacing: 0.5px; line-height: 1; }
  .brand-sub { font-size: 8px; letter-spacing: 2.2px; font-weight: 700; margin-top: 3px; }
  .header .phone { position: absolute; left: 403px; display: flex; align-items: center; gap: 8px; font-size: 15px; font-weight: 300; }
  .header .phone svg { width: 16px; height: 12px; }
  .header .lang { position: absolute; right: 117px; font-size: 10px; letter-spacing: 1px; color: #333; }

  .hero { height: 288px; position: relative; overflow: hidden; }
  .hero-photo { position: absolute; inset: 0; background: linear-gradient(90deg, #cfcfcf 0%, #e9e9e9 30%, #bdbdbd 55%, #d9b15e 70%, #e6be3c 100%); }
  .hero-title { position: absolute; left: 125px; top: 88px; }
  .hero-title .bar { width: 26px; height: 2px; background: var(--gold); margin-bottom: 8px; }
  .hero-title h1 { font-family: "Open Sans", sans-serif; font-weight: 700; font-size: 45px; line-height: 0.95; color: #262626; letter-spacing: -0.5px; }
  .hero-title p { font-family: "Open Sans", sans-serif; font-weight: 300; font-size: 27px; line-height: 1.1; color: #262626; margin-left: 3px; }

  .section { text-align: center; position: relative; }
  .section .mark { width: 22px; height: 22px; background: var(--gold); margin: 0 auto; }
  .section h2 { font-family: "Roboto Condensed", sans-serif; font-weight: 700; font-size: 19px; color: var(--gold); letter-spacing: 0.5px; }
  .section p { font-size: 12px; line-height: 22px; color: #222; }

  .about { height: 233px; padding-top: 54px; }
  .about h2 { margin-top: 26px; }
  .about p { margin-top: 5px; }

  .services { height: 228px; background: var(--cream); border-top: 1px solid #efe3cc; padding-top: 22px; }
  .services h2 { margin-top: 24px; }
  .service-list { position: absolute; top: 112px; left: 117px; right: 117px; }
  .service-list ul { position: absolute; list-style: none; text-align: left; }
  .service-list li { display: flex; align-items: center; gap: 11px; font-size: 12px; height: 27.3px; }
  .service-list svg { width: 14px; height: 11px; }

  .claim { height: 217px; padding-top: 36px; }
  .claim h2 { margin-top: 18px; }
  .claim p { margin-top: 4px; }

  .footer { height: 147px; background: linear-gradient(120deg, #fde3b0 0%, #fcd48e 45%, #fbe0ac 70%, #fccf85 100%); position: relative; font-size: 10px; letter-spacing: 0.3px; }
  .footer .mark { position: absolute; left: 117px; top: 10px; width: 54px; height: 54px; background: var(--yellow); }
  .footer .col { position: absolute; top: 22px; line-height: 14px; }
  .footer .col strong { font-weight: 500; }
  .footer .divider { position: absolute; left: 117px; right: 117px; top: 111px; height: 1px; background: #d9b274; }
  .footer .copy { position: absolute; left: 0; right: 0; top: 123px; text-align: center; font-size: 8px; font-weight: 700; }
</style>
</head>
<body>
  <div class="topbar">
    <div class="item">
      <svg viewBox="0 0 12 12" fill="none" stroke="#e0a33a" stroke-width="1"><circle cx="6" cy="6" r="5"/><ellipse cx="6" cy="6" rx="2.2" ry="5"/><line x1="1" y1="6" x2="11" y2="6"/></svg>
      www.norvatek-systems.de
    </div>
    <div class="item">
      <svg viewBox="0 0 12 9"><rect width="12" height="9" fill="#f2a11d"/><path d="M0 0 L6 5 L12 0" fill="none" stroke="#fff" stroke-width="1"/></svg>
      contact@velunto.de
    </div>
  </div>

  <header class="header">
    <div class="brand">
      <div class="brand-mark"></div>
      <div>
        <div class="brand-name">VELUNTO</div>
        <div class="brand-sub">TRUSTED ADVISORS</div>
      </div>
    </div>
    <div class="phone">
      <svg viewBox="0 0 16 12"><path d="M1 4 Q8 -1 15 4 L13 6 L11 4 L5 4 L3 6 Z" fill="#f2a11d"/><rect x="3" y="6" width="10" height="6" rx="1" fill="#f2a11d"/><circle cx="8" cy="9" r="1.6" fill="#fff"/></svg>
      +49 (7000) 412 558 20
    </div>
    <div class="lang">DE &nbsp;|&nbsp; EN</div>
  </header>

  <section class="hero">
    <div class="hero-photo" role="img" aria-label="Schwarzweißfoto von Beratern am Schreibtisch mit Taschenrechner, Notizblock und Füller, rechts mit goldgelben Dreiecksflächen überlagert"></div>
    <div class="hero-title">
      <div class="bar"></div>
      <h1>VELUNTO</h1>
      <p>TRUSTED ADVISORS</p>
    </div>
  </section>

  <section class="section about">
    <div class="mark"></div>
    <h2>WER SIND WIR?</h2>
    <p>Wir sind ein Unternehmen VELUNTO group und sehen uns als strategische Berater und Planer, professioneller Manager,<br>Controller, Backoffice-Dienstleister und Finanzberater und vieles mehr…</p>
  </section>

  <section class="section services">
    <div class="mark"></div>
    <h2>WAS TUN WIR?</h2>
    <div class="service-list">
      <ul style="left:0">
        <li><svg viewBox="0 0 14 11"><path d="M1 6 L5 10 L13 1" fill="none" stroke="#111" stroke-width="2.4"/></svg>Wealth management</li>
        <li><svg viewBox="0 0 14 11"><path d="M1 6 L5 10 L13 1" fill="none" stroke="#111" stroke-width="2.4"/></svg>Investitionen</li>
        <li><svg viewBox="0 0 14 11"><path d="M1 6 L5 10 L13 1" fill="none" stroke="#111" stroke-width="2.4"/></svg>Beteiligungsmanagement</li>
      </ul>
      <ul style="left:262px; top:-1px">
        <li><svg viewBox="0 0 14 11"><path d="M1 6 L5 10 L13 1" fill="none" stroke="#111" stroke-width="2.4"/></svg>Immobilienmanagement</li>
        <li><svg viewBox="0 0 14 11"><path d="M1 6 L5 10 L13 1" fill="none" stroke="#111" stroke-width="2.4"/></svg>Familiy governance</li>
        <li><svg viewBox="0 0 14 11"><path d="M1 6 L5 10 L13 1" fill="none" stroke="#111" stroke-width="2.4"/></svg>Vermögensplanung</li>
      </ul>
      <ul style="left:494px; top:-1px">
        <li><svg viewBox="0 0 14 11"><path d="M1 6 L5 10 L13 1" fill="none" stroke="#111" stroke-width="2.4"/></svg>Strukturen</li>
        <li><svg viewBox="0 0 14 11"><path d="M1 6 L5 10 L13 1" fill="none" stroke="#111" stroke-width="2.4"/></svg>Nachfolgeplanung</li>
        <li><svg viewBox="0 0 14 11"><path d="M1 6 L5 10 L13 1" fill="none" stroke="#111" stroke-width="2.4"/></svg>Finanzdienstleistungen</li>
      </ul>
    </div>
  </section>

  <section class="section claim">
    <div class="mark"></div>
    <h2>UNSER ANSPRUCH</h2>
    <p>Wir sind für Sie da, damit Sie sich befreit, gesichert und mit voller Konzentration auf<br>Ihre Funktion im eigenen Unternehmen fokussieren können.</p>
  </section>

  <footer class="footer">
    <div class="mark"></div>
    <div class="col" style="left:376px">
      <strong>Velunto Holding GmbH</strong><br>
      Lindenweg 4<br>
      77000 Talbrunn<br>
      contact@velunto.de<br>
      +49 (7000) 412 558 20
    </div>
    <div class="col" style="left:574px">
      <strong>Rechtliches:</strong><br>
      GF: Jonas Feller und Lena Feller<br>
      HRB 700318<br>
      Steuer-Nr.: 14000/60271
    </div>
    <div class="divider"></div>
    <div class="copy">Copyright 2020. All rights reserved.</div>
  </footer>
</body>
</html>
```